New letter head for Air Conditioning business

We need a new professional letter head design to suit our new re-branded air conditioning business. Our new logo is attached

```html
<!DOCTYPE html>
<html lang="en">
<head>
<meta charset="utf-8">
<title>Calvera Letterhead</title>
<link href="https://fonts.googleapis.com/css2?family=Poppins:wght@400;500;600&family=Didact+Gothic&display=swap" rel="stylesheet">
<style>
  :root {
    --paper-light: #f3f3f3;
    --paper: #e4e4e4;
    --ink: #2f2f31;
    --body-ink: #4a4a4c;
    --rule: #8c8c8c;
    --coral: #ee6a5a;
    --green: #5fc181;
    --charcoal: #3c3c3e;
  }
  html, body {
    margin: 0;
    padding: 0;
    width: 960px;
    height: 1200px;
    overflow: hidden;
  }
  .letterhead {
    position: relative;
    width: 960px;
    height: 1200px;
    background: linear-gradient(100deg, var(--paper-light) 0%, var(--paper) 55%, #e0e0e0 100%);
    overflow: hidden;
    color: var(--ink);
  }
  .header {
    position: absolute;
    top: 84px;
    left: 75px;
    right: 20px;
    height: 56px;
    font-family: "Poppins", sans-serif;
  }
  .brand {
    position: absolute;
    left: 0;
    top: 8px;
    display: flex;
    align-items: center;
    gap: 14px;
  }
  .brand-dot {
    width: 42px;
    height: 42px;
    border-radius: 50%;
    background: var(--green);
  }
  .brand-name {
    font-weight: 600;
    font-size: 30px;
    letter-spacing: 3px;
    color: var(--ink);
    text-transform: uppercase;
  }
  .divider {
    position: absolute;
    top: 0;
    width: 1px;
    height: 56px;
    background: var(--rule);
  }
  .divider-one { left: 307px; }
  .divider-two { left: 617px; }
  .address {
    position: absolute;
    left: 362px;
    top: 5px;
    font-style: normal;
    font-size: 14.5px;
    line-height: 18px;
    white-space: nowrap;
  }
  .address .web {
    color: var(--coral);
    font-weight: 600;
    letter-spacing: 0.3px;
  }
  .contact {
    position: absolute;
    left: 663px;
    top: 5px;
    font-size: 14.5px;
    line-height: 18px;
    list-style: none;
    margin: 0;
    padding: 0;
    white-space: nowrap;
  }
  .contact li {
    display: flex;
    align-items: center;
    gap: 8px;
  }
  .contact svg { width: 11px; height: 11px; fill: var(--coral); flex: none; }
  .letter {
    position: absolute;
    left: 87px;
    width: 793px;
    top: 396px;
    font-family: "Didact Gothic", sans-serif;
    color: var(--body-ink);
  }
  .salutation {
    font-family: "Poppins", sans-serif;
    font-weight: 400;
    font-size: 22px;
    line-height: 28px;
    color: var(--ink);
    margin: 0 0 52px;
  }
  .letter p {
    font-size: 14px;
    line-height: 20.6px;
    margin: 0 0 20.6px;
    text-align: justify;
  }
  .letter .closing {
    margin-top: 40px;
  }
  .signature {
    width: 126px;
    height: 72px;
    margin-top: 24px;
    background: linear-gradient(90deg, rgba(47,47,49,0.18), rgba(47,47,49,0.05));
    border-radius: 4px;
  }
  .footer-band {
    position: absolute;
    left: 0;
    bottom: 0;
    width: 960px;
    height: 44px;
    background: var(--charcoal);
  }
</style>
</head>
<body>
<main class="letterhead">
  <header class="header">
    <div class="brand">
      <span class="brand-dot"></span>
      <span class="brand-name">Calvera</span>
    </div>
    <span class="divider divider-one"></span>
    <address class="address">
      1420 Birchwood Court<br>
      Fairbanks, Alaska 99701<br>
      <span class="web">www.calvera-air.com</span>
    </address>
    <span class="divider divider-two"></span>
    <ul class="contact">
      <li><svg viewBox="0 0 24 24"><path d="M6.6 10.8a15.1 15.1 0 0 0 6.6 6.6l2.2-2.2a1 1 0 0 1 1-.25 11.4 11.4 0 0 0 3.6.57 1 1 0 0 1 1 1V20a1 1 0 0 1-1 1A17 17 0 0 1 3 4a1 1 0 0 1 1-1h3.5a1 1 0 0 1 1 1c0 1.25.2 2.45.57 3.57a1 1 0 0 1-.25 1z"/></svg>555-014-2277</li>
      <li><svg viewBox="0 0 24 24"><path d="M6 2h12v6H6zM3 9h18a2 2 0 0 1 2 2v7h-4v4H5v-4H1v-7a2 2 0 0 1 2-2zm4 8v3h10v-3z"/></svg>555-014-2390</li>
      <li><svg viewBox="0 0 24 24"><path d="M2 5h20v14H2zm2 2v.5l8 5 8-5V7z"/></svg>info@calvera-air.com</li>
    </ul>
  </header>

  <section class="letter">
    <h1 class="salutation">Dear Mr. Holloway,</h1>
    <p>Lorem ipsum dolor sit amet, consectetur adipiscing elit. Donec orci purus, luctus vitae dignissim eu, iaculis sed purus. Vivamus faucibus, ipsum nec aliquet viverra, leo mauris condimentum ligula, sit amet sagittis enim ligula quis arcu. Nam egestas tortor id nisi porttitor mattis. In tortor ante, ultricies in suscipit a, tempus non massa. Vivamus et auctor mi. Fusce vel massa nulla. Phasellus nec eros mauris, et scelerisque orci.</p>
    <p>Donec malesuada orci vitae nulla accumsan porta a id massa. Quisque accumsan iaculis magna sit amet fringilla. Maecenas consequat, magna eget tincidunt semper, odio nibh rutrum mi, id feugiat ante nisi eu risus. Vestibulum nunc orci, rhoncus a placerat in, ultricies in mi. Cras mattis varius eros, vel fringilla nisi suscipit eget. Quisque scelerisque sagittis nulla at porttitor.</p>
    <p>Sed id augue vitae urna euismod commodo aliquet a quam. Pellentesque arcu velit, cursus et malesuada ut, consequat et diam. Nullam erat sem, rhoncus id ullamcorper vitae, rhoncus et arcu. In ultricies ultricies nulla, ut rutrum nisi iaculis at. Donec eu magna a metus ornare faucibus. Fusce aliquet faucibus ultricies. Morbi semper, est id tincidunt gravida, sem arcu adipiscing lacus, ac bibendum nulla leo eu purus. Quisque nec diam sed risus consectetur accumsan quis quis nibh. Vestibulum id purus lorem.</p>
    <p>It is a long established fact that a reader will be distracted by the readable content of a page when looking at its layout. The point of using Lorem Ipsum is that it has a more-or-less normal distribution of letters, as opposed to using 'Content here, content here', making it look like readable English. Many desktop publishing packages</p>
    <p class="closing">Sincerely,</p>
    <div class="signature" role="img" aria-label="Handwritten signature of the sender"></div>
  </section>

  <div class="footer-band" role="img" aria-label="Decorative footer band in charcoal with green and coral accents"></div>
</main>
</body>
</html>
```